Business Card Design and a letter head logo

50/50 share milker dairy farmer of 400 cows with a silage and haymaking sideline business
15 years farming currently looking for new opportunities within the dairy farming sector. trying to put together a portfolio to get another 50/50 share milking job aswell

Industry/Entity Type

Farming

Contact Information for Business Card

Birch Farming LTD
Corwin & Felicity Hartley
382 Kelvale Ridge Highway
RD1 Tawhiro 0184
Whangarei
hartley.corwin@lumenmail.co.nz
0273948261
(09) 4715293

```html
<!DOCTYPE html>
<html lang="en">
<head>
<meta charset="utf-8">
<title>Birch Farming LTD – Business Card</title>
<link rel="stylesheet" href="https://fonts.googleapis.com/css2?family=Quattrocento+Sans&display=swap">
<style>
  :root {
    --page-bg: #ecebe8;
    --parchment-light: #c39a5c;
    --parchment-mid: #a87a3e;
    --parchment-dark: #6e4a22;
    --ink: #1c140c;
    --stitch: #1a120a;
    --art-core: #7a5228;
    --art-edge: #9c7038;
  }
  * { margin: 0; padding: 0; box-sizing: border-box; }
  html, body {
    width: 1200px;
    height: 800px;
    overflow: hidden;
    background: var(--page-bg);
  }
  .canvas {
    width: 1200px;
    height: 800px;
    display: flex;
    align-items: center;
    justify-content: center;
  }
  .business-card {
    position: relative;
    width: 1000px;
    height: 638px;
    background: radial-gradient(ellipse at 55% 40%, var(--parchment-light) 0%, var(--parchment-mid) 60%, var(--parchment-dark) 100%);
    font-family: "Quattrocento Sans", sans-serif;
    color: var(--ink);
  }
  .stitch-frame {
    position: absolute;
    inset: 22px;
    border: 4px dashed var(--stitch);
  }
  .cow-illustration {
    position: absolute;
    left: 75px;
    top: 95px;
    width: 340px;
    height: 440px;
    border-radius: 24px;
    background: radial-gradient(ellipse at 50% 50%, var(--art-core) 0%, var(--art-edge) 100%);
  }
  .card-heading {
    position: absolute;
    top: 64px;
    right: 54px;
    font-size: 33px;
    font-weight: 400;
    line-height: 40px;
    white-space: nowrap;
  }
  .contact-block {
    position: absolute;
    right: 58px;
    top: 464px;
    text-align: right;
    font-size: 23px;
    font-style: normal;
    line-height: 30px;
    white-space: nowrap;
  }
</style>
</head>
<body>
<main class="canvas">
  <article class="business-card">
    <div class="stitch-frame"></div>
    <div class="cow-illustration" role="img" aria-label="Logo area: line drawing of a dairy cow looking upward with a curled tail"></div>
    <h1 class="card-heading">Birch Farming LTD Corwin &amp; Felicity</h1>
    <address class="contact-block">
      <div>Hartley 382 Kelvale Ridge Highway</div>
      <div>RD1 Tawhiro 0184</div>
      <div>Whangarei hartley.corwin@lumenmail.co.nz</div>
      <div>0273948261 (09) 4715293</div>
    </address>
  </article>
</main>
</body>
</html>
```